Renewable Energy Consultancy needs relatively simple but smart website

We are a renewable energy focussed consultancy called Brenmoss, and we are just starting out. Our target is to bring knowledge of the detailed technical and commercial operations of renewables projects, mainly wind energy.

Our target customers are major energy utilities and private finance groups, who look to invest in renewables projects as a long term money-earning system. We are a fairly young, dynamic team of industry-respected people (4 of us) but we need to make ourselves look bigger than this (our customers will expect us to take on major projects, so we need to look big enough to handle it...)

We're not going to sell anything from our website and we expect it to just support our company name. Most of our customers are made by strong networks and relationships, so its mainly there to give confidence in our capabilities and give a strong view of who we are. We probably need a site with 4/5 pages which we can then expand when needed.

We have logos and headers (attached) which we want to use (also run through quillmarket), and I've attached a few pictures of projects similar to those we will be involved in to give us a feel for how it will look. Also attached are the colours we liked which are now used in the logo, and the font details. Whilst we're a "green" company with a "green" logo, we don't want to be completely green, so some nice combinations of colours on the pages would be good.

Ideally we need to have flenzo/torvaly news feeds somewhere linked into the site.

The design should be smart - giving a feel of high integrity and assurance whilst making us seem approachable and knowledgeable.

Target Market(s)

Renewables investors, developers of renewables projects (wind farms etc),

Industry/Entity Type

Finance

Coding

Coded - Design and coding required

Number of Pages Required

4 page

Other font styles liked:
• See the attachment with brand text/colour details ("colour codes" filename)

Requirements
Must have
• A fairly simple, but smart website design. We're looking to provide confidence and consolidate our networks with the website, not specifically find new customers - so its really just to give customers somewhere they can relate to online
Nice to have
• We have logos/brands and colours - so a website which incorperates these well and brings accross a professional company
• Would be nice to have a page (such as a blog/wordpress) we can easily update with news/events etc and links to flenzo feed and torvaly feed ideally.
Should not have
• cartoons, flashy gimmicks,

```html
<!DOCTYPE html>
<html lang="en">
<head>
<meta charset="utf-8">
<title>Brenmoss — Renewable Energy Consultancy</title>
<link rel="stylesheet" href="https://fonts.googleapis.com/css2?family=Montserrat:wght@300;400;600;700&family=Gelasio:wght@400&display=swap">
<style>
  :root{
    --green:#6aa600;
    --green-light:#8cc43f;
    --green-dark:#1f4d0c;
    --green-deep:#225010;
    --grey-bg:#eeeeee;
    --grey-diamond:#5e5e5e;
    --ink:#222;
    --white:#fff;
  }
  *{margin:0;padding:0;box-sizing:border-box}
  html,body{width:914px;height:1200px;overflow:hidden}
  body{position:relative;font-family:"Montserrat",sans-serif;background:var(--white);color:var(--ink)}
  .abs{position:absolute}

  /* hero */
  .hero-photo{left:0;top:0;width:914px;height:520px;
    background:linear-gradient(180deg,#1d2340 0%,#2e3552 30%,#5b4a4a 55%,#b4552a 72%,#e0781c 80%,#3a2a2a 100%)}
  .brand{left:58px;top:16px;display:flex;align-items:center;gap:10px}
  .brand-dot{width:32px;height:32px;border-radius:50%;background:var(--white)}
  .brand-name{font-size:26px;font-weight:400;color:var(--white);letter-spacing:.5px}
  .nav{left:413px;top:28px;display:flex;gap:21px;font-size:7.5px;font-weight:700;letter-spacing:.3px}
  .nav a{color:var(--green-light);text-decoration:none}
  .nav a.active{color:var(--white);border-bottom:1.5px solid var(--white);padding-bottom:4px}
  .social{display:flex;gap:8px;font-size:8px;font-weight:700;color:var(--green-light)}
  .social-top{left:712px;top:28px}
  .menu-icon{left:847px;top:26px}

  .hero-mark{left:395px;top:132px;width:110px;height:110px;border-radius:50%;background:var(--green);
    display:flex;align-items:center;justify-content:center;color:var(--white);font-size:17px;font-weight:600}
  .slide-arrow{top:252px;width:55px;height:55px;border-radius:50%;background:rgba(150,150,150,.55)}
  .slide-arrow.prev{left:65px}.slide-arrow.next{left:798px}
  .slide-arrow svg{position:absolute;left:0;top:0}
  .hero-title{left:130px;top:268px;width:627px;height:39px;background:rgba(30,30,30,.75);
    font-size:31px;line-height:39px;text-align:center;color:var(--green-light);font-weight:300;letter-spacing:.5px}
  .hero-title strong{font-weight:700}
  .hero-sub{left:0;width:914px;top:312px;text-align:center;font-size:20px;font-weight:300;color:var(--green);letter-spacing:1px}
  .btn{left:385px;top:369px;width:133px;height:31px;background:var(--green);color:#111;font-size:10px;
    text-align:center;line-height:31px;letter-spacing:.3px}

  /* concept */
  .concept-band{left:0;top:0}
  .turbine-art{left:640px;top:460px;width:200px;height:265px;
    background:linear-gradient(180deg,rgba(40,80,10,0) 0%,rgba(40,80,10,.18) 100%)}
  .section-title{left:0;width:914px;text-align:center;font-weight:700;color:var(--green-dark);letter-spacing:1px}
  .concept-title{top:538px;font-size:32px}
  .concept-text{left:257px;top:580px;width:400px;text-align:center;font-family:"Gelasio",serif;font-size:12px;line-height:19px;color:#1a2a10}
  .rule{width:1px;background:#333}
  .diamond{width:115px;height:32px}
  .diamond span{position:absolute;left:0;top:0;width:115px;height:32px;display:flex;align-items:center;justify-content:center;
    text-align:center;font-size:8px;color:var(--white);line-height:10px;letter-spacing:.3px}

  /* customers */
  .customers{left:0;top:725px;width:914px;height:402px;background:var(--grey-bg)}
  .customers-title{top:776px;font-size:32px}
  .customer{top:852px;width:134px;text-align:center}
  .customer-photo{width:134px;height:134px;border-radius:50%;border:4px solid #7a9a2a}
  .customer-label{margin-top:8px;font-size:10.5px;color:#222;letter-spacing:.3px}

  /* footer */
  .copyright{left:150px;top:1162px;font-size:6.5px;color:#555}
  .foot-mark{left:437px;top:1143px;width:36px;height:36px;border-radius:50%;background:var(--green);
    display:flex;align-items:center;justify-content:center;color:var(--white);font-size:5.5px;font-weight:600}
  .social-foot{left:712px;top:1162px;font-size:9px;color:var(--green-deep)}
</style>
</head>
<body>

<!-- hero -->
<div class="abs hero-photo" role="img" aria-label="Wind turbines silhouetted against a sunset sky over hills"></div>

<div class="abs brand"><span class="brand-dot"></span><span class="brand-name">Brenmoss</span></div>
<nav class="abs nav">
  <a class="active" href="#">HOME</a><a href="#">SERVICES</a><a href="#">DEVELOPERS</a><a href="#">CLIENTS</a><a href="#">CONTACT</a>
</nav>
<div class="abs social social-top"><span>kindrel</span><span>flenzo</span><span>torvaly</span></div>
<svg class="abs menu-icon" width="16" height="14" viewBox="0 0 16 14"><g stroke="#8cc43f" stroke-width="1.6"><line x1="0" y1="2" x2="16" y2="2"/><line x1="0" y1="5.5" x2="16" y2="5.5"/><line x1="0" y1="9" x2="16" y2="9"/><line x1="0" y1="12.5" x2="16" y2="12.5"/></g></svg>

<div class="abs hero-mark">Brenmoss</div>
<div class="abs slide-arrow prev"><svg width="55" height="55"><polyline points="32,16 22,27.5 32,39" fill="none" stroke="#ddd" stroke-width="1.2"/></svg></div>
<div class="abs slide-arrow next"><svg width="55" height="55"><polyline points="23,16 33,27.5 23,39" fill="none" stroke="#ddd" stroke-width="1.2"/></svg></div>
<h1 class="abs hero-title">RENEWABLE ENERGY <strong>WIND POWER</strong></h1>
<p class="abs hero-sub">CLEAN AND AFFORDABLE</p>
<a class="abs btn">VIEW OUR PROJECTS</a>

<!-- concept -->
<svg class="abs concept-band" width="914" height="725"><polygon points="0,505 914,400 914,725 0,725" fill="#6aa600"/></svg>
<div class="abs turbine-art" role="img" aria-label="Silhouettes of wind turbines"></div>
<svg class="abs" style="left:440px;top:462px" width="32" height="70">
  <circle cx="15.5" cy="15.5" r="14" fill="none" stroke="#1f4d0c" stroke-width="1.5"/>
  <polyline points="9,13 15.5,19 22,13" fill="none" stroke="#1f4d0c" stroke-width="1.5"/>
  <polyline points="9,9 15.5,15 22,9" fill="none" stroke="#1f4d0c" stroke-width="1.5"/>
  <line x1="15.5" y1="30" x2="15.5" y2="68" stroke="#1f4d0c"/>
</svg>
<h2 class="abs section-title concept-title">CONCEPT</h2>
<p class="abs concept-text">We are a renewable energy focussed consultancy called Brenmoss, and we are just starting out. Our target is to bring knowledge of the detailed technical and commercial operations of renewables projects, mainly wind energy.</p>
<div class="abs rule" style="left:455px;top:647px;height:26px"></div>
<div class="abs diamond" style="left:398px;top:672px">
  <svg width="115" height="32"><polygon points="0,16 20,0 95,0 115,16 95,32 20,32" fill="#5e5e5e"/></svg>
  <span>READ MORE</span>
</div>

<!-- customers -->
<section class="abs customers"></section>
<div class="abs rule" style="left:455px;top:734px;height:36px"></div>
<h2 class="abs section-title customers-title">OUR TARGET CUSTOMERS</h2>

<div class="abs customer" style="left:155px">
  <div class="customer-photo" role="img" aria-label="Wind farm with hay bales in a field" style="background:linear-gradient(180deg,#b9d3ea 0%,#8fb4d6 60%,#6f8a52 100%)"></div>
  <p class="customer-label">WIND FARMS</p>
</div>
<div class="abs customer" style="left:312px">
  <div class="customer-photo" role="img" aria-label="Offshore turbine under construction at sea" style="background:linear-gradient(180deg,#5b6470 0%,#3e4a57 55%,#2f4e66 100%)"></div>
  <p class="customer-label">DEVELOPERS</p>
</div>
<div class="abs customer" style="left:464px">
  <div class="customer-photo" role="img" aria-label="Operators standing beside wind turbines" style="background:linear-gradient(180deg,#3c6ec0 0%,#6d9ad6 60%,#1e2a3a 100%)"></div>
  <p class="customer-label">OPERATORS</p>
</div>
<div class="abs customer" style="left:623px">
  <div class="customer-photo" role="img" aria-label="Group of business owners in an office" style="background:linear-gradient(180deg,#dfe6ec 0%,#b8c4cc 55%,#3a3f48 100%)"></div>
  <p class="customer-label">OWNERS</p>
</div>

<div class="abs rule" style="left:455px;top:1040px;height:26px"></div>
<div class="abs diamond" style="left:398px;top:1065px">
  <svg width="115" height="32"><polygon points="0,16 20,0 95,0 115,16 95,32 20,32" fill="#225010"/></svg>
  <span>PROJECTS<br>GALLERY</span>
</div>

<!-- footer -->
<footer>
  <p class="abs copyright">© 2015 Brenmoss. All Rights Reserved</p>
  <div class="abs foot-mark">Brenmoss</div>
  <div class="abs social social-foot"><span>flenzo</span><span>torvaly</span></div>
</footer>

</body>
</html>
```